Demo Screens Needed for Recruiting with AI App

We are in the process of raising money for our startup called PylonGrove. We need demos to show investors what we're trying to do with images. We really love the simplicity and modern look of the Lantern App and want something similar. We will have the "swipe" functionality similar to Kindle as well. The sample images I've attached are only for caregivers but long term this will be for all industries. There will also be a rewards page for loyalty membership. The current landing page is www.pylongrove.example. That will show you the color scheme and logo.

```html
<!DOCTYPE html>
<html lang="en">
<head>
<meta charset="utf-8">
<title>PylonGrove – Caregiver Matching Screens</title>
<link rel="stylesheet" href="https://fonts.googleapis.com/css2?family=Figtree:wght@300;400;500;600&display=swap">
<style>
:root{
  --stage:#031a23;
  --ink:#0b1a22;
  --muted:#6b7780;
  --accent:#0a86bd;
  --accent-soft:#bfe9f7;
  --sky:#4fc3ec;
  --navy:#04202c;
  --line:#cfdbe1;
  --star:#f5c518;
  --white:#ffffff;
}
*{box-sizing:border-box;margin:0;padding:0}
html,body{width:1200px;height:900px;overflow:hidden;background:var(--stage);font-family:"Figtree",sans-serif;color:var(--ink)}
.phone{position:absolute;top:166px;width:262px;height:568px;border-radius:26px;overflow:hidden;background:var(--white)}
.p1{left:36px}.p2{left:325px}.p3{left:613px}.p4{left:902px}
.abs{position:absolute}
.status{position:absolute;top:12px;left:0;right:0;height:16px;font-size:11px;font-weight:600}
.status .time{position:absolute;left:36px;top:2px}
.status svg{position:absolute;right:22px;top:3px}
.home-bar{position:absolute;bottom:7px;left:50%;width:92px;height:3px;margin-left:-46px;border-radius:2px;background:var(--ink)}
.photo{position:absolute}
/* welcome */
.p1{background:var(--navy);color:var(--white)}
.p1 .photo{inset:0;background:linear-gradient(170deg,#27495a 0%,#1b3847 35%,#0b2532 65%,#04141c 100%)}
.wordmark{position:absolute;top:270px;left:0;right:0;text-align:center;font-size:25px;font-weight:300;letter-spacing:3px;color:var(--white)}
.tagline{position:absolute;top:314px;left:0;right:0;text-align:center;font-size:16px;font-weight:300;line-height:19px}
.tagline em{font-style:normal;color:var(--sky)}
.cta{position:absolute;top:383px;left:49px;width:163px;height:31px;border-radius:16px;background:var(--accent);color:var(--white);font-size:10px;font-weight:500;display:flex;align-items:center;justify-content:center;letter-spacing:.2px}
.login-row{position:absolute;top:511px;left:16px;right:16px;display:flex;justify-content:space-between;align-items:center;font-size:10.5px;font-weight:600}
.login{height:31px;width:76px;border-radius:16px;background:#0a2633;color:var(--sky);display:flex;align-items:center;justify-content:center;gap:5px;font-size:10px}
.p1 .home-bar{background:var(--white)}
/* header */
.topbar{position:absolute;top:42px;left:0;right:0;height:20px;text-align:center;font-size:12px;font-weight:500}
.topbar .back{position:absolute;left:13px;top:2px}
.topbar .menu{position:absolute;right:16px;top:1px}
/* filters */
.chips{position:absolute;top:73px;left:10px;display:flex;gap:6px;white-space:nowrap}
.chip{height:27px;border:1px solid var(--line);border-radius:14px;display:flex;align-items:center;gap:5px;padding:0 9px;font-size:9px;color:var(--muted)}
.fade-band{position:absolute;top:104px;left:0;right:0;height:12px;background:linear-gradient(#e9f3f7,#fff)}
.card{position:absolute;left:6px;width:250px;height:82px}
.card .photo{left:0;top:0;width:80px;height:80px;background:linear-gradient(135deg,#8a6a55,#c9a48a 55%,#d9d2c8)}
.card .name{position:absolute;left:91px;top:2px;font-size:13.5px}
.card .loc{position:absolute;left:91px;top:23px;font-size:9px;color:var(--muted)}
.card .rate{position:absolute;right:6px;top:5px;font-size:9px;color:var(--muted);display:flex;gap:3px;align-items:center}
.card .rating{position:absolute;right:0;top:23px;font-size:9px;color:var(--muted);display:flex;gap:3px;align-items:center}
.card .blurb{position:absolute;left:91px;top:47px;width:160px;font-size:9.8px;line-height:14.6px;color:#2a3840}
.card .blurb b{font-weight:500;color:var(--ink)}
.stars{color:var(--star);letter-spacing:-.5px;font-size:10px}
.stars i{font-style:normal;color:#d8dde0}
.faded{opacity:.35}
.nav{position:absolute;left:0;right:0;top:512px;height:36px;display:flex;justify-content:space-around;align-items:center;padding:0 10px}
.nav .on{width:32px;height:32px;border-radius:50%;background:var(--accent-soft);display:flex;align-items:center;justify-content:center}
.nav-fade{position:absolute;left:0;right:0;top:490px;height:78px;background:linear-gradient(rgba(255,255,255,0),#fff 35%)}
/* profile */
.who{position:absolute;top:62px;left:11px;font-size:22px;font-weight:400}
.head-icons{position:absolute;top:67px;right:14px;display:flex;gap:16px}
.p3 .photo.hero{top:94px;left:0;width:262px;height:242px;background:radial-gradient(ellipse at 50% 55%,#b07a5b 0%,#8e6047 30%,#b9b6b3 60%,#d2d0ce 100%)}
.online{position:absolute;top:101px;left:6px;height:28px;padding:0 11px;border-radius:14px;background:var(--navy);color:var(--white);font-size:9.5px;display:flex;align-items:center;gap:7px;letter-spacing:.4px}
.online span{width:9px;height:9px;border-radius:50%;background:var(--sky);border:2px solid #1e6f8f}
.prompt{position:absolute;top:358px;left:16px;font-size:10px;font-weight:500}
.answer{position:absolute;top:378px;left:16px;width:236px;font-size:17px;font-weight:300;line-height:21.4px;color:#2a3840}
.answer .dim{color:#7b878e}
.actions{position:absolute;left:12px;right:12px;top:470px;height:32px;display:flex;justify-content:space-between;align-items:center}
.pass,.like{width:53px;height:32px;border-radius:16px;display:flex;align-items:center;justify-content:center;gap:3px}
.pass{background:var(--white);box-shadow:0 2px 8px rgba(0,30,45,.12)}
.like{background:var(--navy)}
.profile-btn{width:86px;height:32px;border-radius:16px;background:var(--white);box-shadow:0 2px 8px rgba(0,30,45,.12);font-size:9.5px;letter-spacing:1px;display:flex;align-items:center;justify-content:center}
/* details */
.summary{position:absolute;top:65px;left:0;right:0;height:46px;background:var(--navy);color:var(--white);font-size:10.5px;font-weight:300;padding:8px 16px;line-height:16px}
.summary .right{position:absolute;right:16px;top:8px;text-align:right}
.facts{position:absolute;top:132px;left:22px;right:10px;list-style:none}
.facts li{height:31px;display:flex;align-items:center;gap:9px;font-size:9.5px}
.facts li span+span{margin-left:-3px}
.p4 .photo.bottom{top:352px;left:0;width:262px;height:216px;background:radial-gradient(ellipse at 45% 55%,#c99378 0%,#8c5532 35%,#5b4a3a 60%,#9a9a90 100%)}
.p4 .actions{top:512px}
.p4 .home-bar{background:var(--white)}
</style>
</head>
<body>

<svg width="0" height="0" style="position:absolute">
  <defs>
    <g id="ic-status">
      <rect x="0" y="6" width="2.5" height="3" rx=".5"/><rect x="3.6" y="4.5" width="2.5" height="4.5" rx=".5"/><rect x="7.2" y="2.5" width="2.5" height="6.5" rx=".5"/><rect x="10.8" y="0.5" width="2.5" height="8.5" rx=".5"/>
      <path d="M18 3.2a8 8 0 0 1 10 0l-1 1.1a6.5 6.5 0 0 0-8 0zM19.8 5.2a5 5 0 0 1 6.4 0l-1 1.1a3.6 3.6 0 0 0-4.4 0zM23 9l-1.6-1.7a2.4 2.4 0 0 1 3.2 0z"/>
      <rect x="32" y="1" width="15" height="7.5" rx="2"/><rect x="48" y="3.5" width="1.3" height="2.5" rx=".6"/>
    </g>
  </defs>
</svg>

<!-- Screen 1: welcome -->
<section class="phone p1">
  <div class="photo" role="img" aria-label="Photo of two people leaning their heads together outdoors, in dark teal tones"></div>
  <div class="status"><span class="time" style="color:#fff">9:41</span><svg width="50" height="10" fill="#fff"><use href="#ic-status"/></svg></div>
  <div class="wordmark">PylonGrove</div>
  <p class="tagline">Unlocking <em>The Power Of</em><br>Meaningful <em>Connections.</em></p>
  <div class="cta">CREATE TRIBE ACCOUNT</div>
  <div class="login-row"><span>Already have an account?</span><span class="login">LOGIN <svg width="10" height="8" fill="none" stroke="#4fc3ec" stroke-width="1.2"><path d="M1 1l3 3-3 3M5 1l3 3-3 3"/></svg></span></div>
  <div class="home-bar"></div>
</section>

<!-- Screen 2: search list -->
<section class="phone p2">
  <div class="status"><span class="time">9:41</span><svg width="50" height="10" fill="#0b1a22"><use href="#ic-status"/></svg></div>
  <div class="topbar">
    <svg class="back" width="14" height="10" fill="none" stroke="#0b1a22" stroke-width="1.3"><path d="M13 5H1M5 1L1 5l4 4"/></svg>
    Find Your Tribe
  </div>
  <div class="chips">
    <div class="chip"><svg width="10" height="12" fill="none" stroke="#0a86bd"><path d="M5 11S1 7 1 4.5a4 4 0 0 1 8 0C9 7 5 11 5 11z"/><circle cx="5" cy="4.5" r="1.3"/></svg>Palo Alto, 15 mi</div>
    <div class="chip"><svg width="11" height="11" fill="none" stroke="#0a86bd"><path d="M1 1h5l4 4-5 5-4-4z"/><circle cx="3.5" cy="3.5" r=".8"/></svg>$25/hr</div>
    <div class="chip"><svg width="11" height="11" fill="none" stroke="#0a86bd"><rect x="1" y="1" width="9" height="6" rx="1"/><path d="M3 7v3l3-3"/></svg>Date</div>
    <div class="chip"><svg width="11" height="11" fill="none" stroke="#0a86bd"><circle cx="5.5" cy="5.5" r="4.5"/><path d="M3.5 5.5l1.5 1.5 2.5-3"/></svg></div>
  </div>
  <div class="fade-band"></div>

  <article class="card" style="top:132px">
    <div class="photo" role="img" aria-label="Portrait of a smiling woman with curly hair"></div>
    <div class="name">Jules M.</div><div class="loc">Palo Alto, CA</div>
    <div class="rate">◇ $25/hr</div>
    <div class="rating"><span class="stars">★★★★<i>★</i></span>(16)</div>
    <p class="blurb"><b>One thing I prioritize in childcare</b> is Creating fun and engaging atmosphere, where children ...</p>
  </article>
  <article class="card" style="top:225px">
    <div class="photo" role="img" aria-label="Photo of two people embracing outdoors" style="background:linear-gradient(135deg,#2c3a44,#6b5a4c 55%,#b79a86)"></div>
    <div class="name">Charlize J.</div><div class="loc">Palo Alto, CA</div>
    <div class="rate">◇ $25/hr</div>
    <div class="rating"><span class="stars">★★★<i>★★</i></span>(10)</div>
    <p class="blurb"><b>An ideal playdate to me is</b> active play, exploration and creativity, such as running around the ...</p>
  </article>
  <article class="card" style="top:318px">
    <div class="photo" role="img" aria-label="Portrait of a smiling man with short dark hair" style="background:linear-gradient(135deg,#bdbab6,#9b6b4f 50%,#7a5440)"></div>
    <div class="name">Joe M.</div><div class="loc">Palo Alto, CA</div>
    <div class="rate">◇ $25/hr</div>
    <div class="rating"><span class="stars">★★★★★</span>(16)</div>
    <p class="blurb"><b>When it comes to meal prep,</b> I excel at making themed dinners such as Meatless Mondays and ...</p>
  </article>
  <article class="card" style="top:411px">
    <div class="photo" role="img" aria-label="Portrait of a woman with long curly hair"></div>
    <div class="name">Ana V.</div><div class="loc">Palo Alto, CA</div>
    <div class="rate">◇ $25/hr</div>
    <div class="rating"><span class="stars">★★★★<i>★</i></span>(10)</div>
    <p class="blurb"><b>When it comes to meal prep,</b> I excel at making themed dinners such as Taco Tuesdays and ...</p>
  </article>
  <article class="card faded" style="top:504px">
    <div class="photo" role="img" aria-label="Portrait of a smiling woman with curly hair"></div>
    <div class="name">Jules M.</div><div class="loc">Palo Alto, CA</div>
    <div class="rate">◇ $25/hr</div>
    <div class="rating"><span class="stars">★★★★<i>★</i></span>(16)</div>
    <p class="blurb">One thing I prioritize in childcare</p>
  </article>
  <div class="nav-fade"></div>
  <nav class="nav">
    <span class="on"><svg width="14" height="13" fill="none" stroke="#0a86bd" stroke-width="1.2"><path d="M1 12L7 1l6 11zM7 6l-2.5 6M7 6l2.5 6"/></svg></span>
    <svg width="14" height="14" fill="none" stroke="#0a86bd" stroke-width="1.1"><path d="M7 1l1.6 4.4L13 7l-4.4 1.6L7 13l-1.6-4.4L1 7l4.4-1.6z"/></svg>
    <svg width="15" height="14" fill="none" stroke="#0a86bd" stroke-width="1.1"><path d="M2 1h11a1 1 0 0 1 1 1v7a1 1 0 0 1-1 1H6l-3 3v-3H2a1 1 0 0 1-1-1V2a1 1 0 0 1 1-1z"/></svg>
    <svg width="14" height="14" fill="none" stroke="#0a86bd" stroke-width="1.1"><circle cx="6" cy="6" r="5"/><path d="M9.5 9.5L13 13"/></svg>
    <svg width="13" height="14" fill="none" stroke="#0a86bd" stroke-width="1.1"><circle cx="6.5" cy="4" r="3"/><path d="M1 13.5c0-3 2.5-5 5.5-5s5.5 2 5.5 5"/></svg>
  </nav>
  <div class="home-bar"></div>
</section>

<!-- Screen 3: swipe card -->
<section class="phone p3">
  <div class="status"><span class="time">9:41</span><svg width="50" height="10" fill="#0b1a22"><use href="#ic-status"/></svg></div>
  <svg class="abs" style="top:46px;left:13px" width="14" height="10" fill="none" stroke="#0b1a22" stroke-width="1.3"><path d="M13 5H1M5 1L1 5l4 4"/></svg>
  <h1 class="who">Joe</h1>
  <div class="head-icons">
    <svg width="15" height="14" fill="none" stroke="#0b1a22" stroke-width="1.1"><path d="M2 1h11a1 1 0 0 1 1 1v7a1 1 0 0 1-1 1H6l-3 3v-3H2a1 1 0 0 1-1-1V2a1 1 0 0 1 1-1z"/><circle cx="5" cy="5.5" r=".6"/><circle cx="7.5" cy="5.5" r=".6"/><circle cx="10" cy="5.5" r=".6"/></svg>
    <svg width="13" height="13" fill="none" stroke="#0b1a22" stroke-width="1.1"><rect x="1" y="1" width="11" height="11" rx="3"/><circle cx="4" cy="6.5" r=".6"/><circle cx="6.5" cy="6.5" r=".6"/><circle cx="9" cy="6.5" r=".6"/></svg>
  </div>
  <div class="photo hero" role="img" aria-label="Portrait of a smiling man against a grey stone wall"></div>
  <div class="online"><span></span>Online</div>
  <p class="prompt">One thing I prioritize in childcare is</p>
  <p class="answer">Creating fun and engaging atmosphere where children can explore, play, and express <span class="dim">themselves creatively.</span></p>
  <div class="actions">
    <span class="pass"><svg width="12" height="12" stroke="#0b1a22" stroke-width="1.4"><path d="M1 1l10 10M11 1L1 11"/></svg><svg width="11" height="8" fill="none" stroke="#8a969c"><path d="M4 1L1 4l3 3M7 1L4 4l3 3M10 1L7 4l3 3"/></svg></span>
    <span class="profile-btn">PROFILE</span>
    <span class="like"><svg width="9" height="8" fill="none" stroke="#4fc3ec"><path d="M1 1l3 3-3 3M5 1l3 3-3 3"/></svg><svg width="15" height="13" fill="none" stroke="#4fc3ec" stroke-width="1.3"><path d="M7.5 12S1 8 1 4.2A3 3 0 0 1 7.5 3a3 3 0 0 1 6.5 1.2C14 8 7.5 12 7.5 12z"/></svg></span>
  </div>
  <nav class="nav">
    <svg width="14" height="13" fill="none" stroke="#0a86bd" stroke-width="1.1"><path d="M1 12L7 1l6 11zM7 6l-2.5 6M7 6l2.5 6"/></svg>
    <span class="on"><svg width="14" height="14" fill="none" stroke="#0a86bd" stroke-width="1.2"><path d="M7 1l1.6 4.4L13 7l-4.4 1.6L7 13l-1.6-4.4L1 7l4.4-1.6z"/></svg></span>
    <svg width="17" height="16" fill="none" stroke="#0a86bd" stroke-width="1.1"><path d="M2 3h11a1 1 0 0 1 1 1v7a1 1 0 0 1-1 1H6l-3 3v-3H2a1 1 0 0 1-1-1V4a1 1 0 0 1 1-1z"/><circle cx="14.5" cy="2" r="2" fill="#1ba7e0" stroke="none"/></svg>
    <svg width="14" height="14" fill="none" stroke="#0a86bd" stroke-width="1.1"><circle cx="6" cy="6" r="5"/><path d="M9.5 9.5L13 13"/></svg>
    <svg width="13" height="14" fill="none" stroke="#0a86bd" stroke-width="1.1"><circle cx="6.5" cy="4" r="3"/><path d="M1 13.5c0-3 2.5-5 5.5-5s5.5 2 5.5 5"/></svg>
  </nav>
  <div class="home-bar"></div>
</section>

<!-- Screen 4: profile details -->
<section class="phone p4">
  <div class="status"><span class="time">9:41</span><svg width="50" height="10" fill="#0b1a22"><use href="#ic-status"/></svg></div>
  <div class="topbar">
    <svg class="back" width="14" height="10" fill="none" stroke="#0b1a22" stroke-width="1.3"><path d="M13 5H1M5 1L1 5l4 4"/></svg>
    Jules
    <svg class="menu" width="13" height="13" fill="none" stroke="#0b1a22" stroke-width="1.1"><rect x="1" y="1" width="11" height="11" rx="3"/><circle cx="4" cy="6.5" r=".6"/><circle cx="6.5" cy="6.5" r=".6"/><circle cx="9" cy="6.5" r=".6"/></svg>
  </div>
  <div class="summary">
    10 yrs experience<br>Female
    <div class="right">$25-$35/hr<br><span class="stars" style="font-size:11px">★★★★<i style="color:#fff">★</i></span></div>
  </div>
  <ul class="facts">
    <li><svg width="12" height="13" fill="none" stroke="#0a86bd"><path d="M6 12S1.5 8 1.5 5a4.5 4.5 0 0 1 9 0C10.5 8 6 12 6 12z"/><circle cx="6" cy="5" r="1.4"/></svg>Palo Alto, California</li>
    <li><svg width="13" height="13" fill="none" stroke="#0a86bd"><circle cx="6.5" cy="6.5" r="5.5"/><path d="M1 6.5h11M6.5 1c-3 3-3 8 0 11M6.5 1c3 3 3 8 0 11"/></svg><span>English</span>&nbsp;<span>Spanish</span>&nbsp;<span>Mandarin</span></li>
    <li><svg width="13" height="13" fill="none" stroke="#0a86bd"><path d="M6.5 1l1.6 1.3 2 .1.4 2 1.3 1.6-1.3 1.6-.4 2-2 .1-1.6 1.3-1.6-1.3-2-.1-.4-2L1.2 6l1.3-1.6.4-2 2-.1z"/><path d="M4.5 6.5l1.5 1.5 2.5-3"/></svg>Bachelor’s Degree</li>
    <li><svg width="13" height="13" fill="none" stroke="#0a86bd"><path d="M1 1h2l1 6h7l1-4H7M4 7l-1 3h8"/><circle cx="4" cy="11.5" r="1"/><circle cx="10" cy="11.5" r="1"/></svg>0-11 mo&nbsp;&nbsp;1-3 yrs&nbsp;&nbsp;4-5 yrs</li>
    <li><svg width="13" height="13" fill="none" stroke="#0a86bd"><rect x="1" y="4" width="11" height="8" rx="1"/><path d="M4.5 4V2h4v2"/></svg>CPR Trained&nbsp;&nbsp;Special Needs Care</li>
    <li><svg width="13" height="13" fill="none" stroke="#0a86bd"><path d="M6.5 1a5.5 5.5 0 1 1-5.5 5.5" stroke-dasharray="2 1.5"/><path d="M6.5 3.5v3l2 1.5"/></svg>Full Time&nbsp;&nbsp;Open to part time</li>
    <li><svg width="13" height="13" fill="none" stroke="#0a86bd"><circle cx="6.5" cy="6.5" r="5.5"/><path d="M6.5 4v5M4 6.5h5"/></svg>Comfortable with pets&nbsp;&nbsp;Meals prep</li>
  </ul>
  <div class="photo bottom" role="img" aria-label="Photo of a laughing woman with curly hair"></div>
  <div class="actions">
    <span class="pass" style="width:53px"><svg width="12" height="12" stroke="#0b1a22" stroke-width="1.4"><path d="M1 1l10 10M11 1L1 11"/></svg><svg width="11" height="8" fill="none" stroke="#8a969c"><path d="M4 1L1 4l3 3M7 1L4 4l3 3M10 1L7 4l3 3"/></svg></span>
    <svg width="8" height="10" fill="none" stroke="#fff" stroke-width="1"><path d="M1 5l3-3 3 3M1 9l3-3 3 3"/></svg>
    <span class="like"><svg width="9" height="8" fill="none" stroke="#4fc3ec"><path d="M1 1l3 3-3 3M5 1l3 3-3 3"/></svg><svg width="15" height="13" fill="none" stroke="#4fc3ec" stroke-width="1.3"><path d="M7.5 12S1 8 1 4.2A3 3 0 0 1 7.5 3a3 3 0 0 1 6.5 1.2C14 8 7.5 12 7.5 12z"/></svg></span>
  </div>
  <div class="home-bar"></div>
</section>

</body>
</html>
```